New Website Design for Rides for Heroes.org - A Site for People to Donate Cars to War / Disabled Ve

Current site: www.ridesforheroes.org; Look at these sites for ideas: bikez2tots.org; gearsforhopes.org; www.autosformarines.org; www.trucksforsoldiers.org

Industry/Entity Type

Charity

Coding

Coded - Design and coding required

Number of Pages Required

1 page

Requirements
Must have
• n/a
Nice to have
• n/a
Should not have
• n/a

```html
<!DOCTYPE html>
<html lang="en">
<head>
<meta charset="utf-8">
<title>Rides for Heroes – Car Donation</title>
<link href="https://fonts.googleapis.com/css2?family=Roboto:wght@400;500;700&family=Roboto+Condensed:wght@400;500&display=swap" rel="stylesheet">
<style>
:root{
  --blue:#2a5cae;
  --blue-dark:#1f4a93;
  --red:#c0262d;
  --green:#6cc237;
  --ink:#222;
  --muted:#555;
  --grey-bg:#e9e9ec;
  --line:#c9c9cc;
}
*{box-sizing:border-box;margin:0;padding:0}
html,body{width:801px;height:1200px;overflow:hidden;background:#fff}
body{font-family:"Roboto",Arial,sans-serif;color:var(--ink);position:relative}
.abs{position:absolute}

/* header */
.brand{left:106px;top:14px;display:flex;align-items:center;gap:6px}
.brand-mark{width:16px;height:16px;border-radius:50%;background:var(--red)}
.brand-name{font-size:15px;font-weight:700;color:var(--blue)}
.help{left:535px;top:12px;font-size:6.5px;letter-spacing:.6px;color:#555;font-weight:500}
.help-phone{left:518px;top:20px;display:flex;align-items:center;gap:5px;font-family:"Roboto Condensed",sans-serif;font-size:15px;color:var(--blue)}
.help-days{left:535px;top:41px;font-size:7px;letter-spacing:1.4px;color:#555;font-weight:500}
.ribbon{left:633px;top:0}

/* nav */
.nav{left:0;top:61px;width:801px;height:22px;background:var(--blue)}
.nav a{position:absolute;top:0;height:22px;line-height:22px;font-size:7px;font-weight:700;color:#fff;text-decoration:none}
.nav .active{background:var(--red);padding:0 10px;left:106px}

/* hero */
.hero{left:0;top:83px;width:801px;height:310px;background:linear-gradient(90deg,#b8423f 0%,#8c5b4c 35%,#5e5550 55%,#7d7f84 75%,#4d4a48 100%)}
.form{left:107px;top:120px;width:236px;height:230px;background:rgba(240,240,240,.93);border:2px solid #d8d8d8}
.form h2{position:absolute;left:0;width:100%;top:17px;text-align:center;font-size:14px;font-weight:400;color:var(--red)}
.field{position:absolute;width:100px;height:22px;border:1px solid #cfcfcf;background:#f4f4f4;font-size:6.5px;color:#444;display:flex;align-items:center;padding-left:7px;gap:7px}
.field svg{flex:none}
.donate-btn{position:absolute;left:14px;top:179px;width:207px;height:28px;border-radius:5px;background:var(--green);color:#fff;font-weight:700;font-size:12px;text-align:center;line-height:28px;letter-spacing:.4px}
.dots{left:363px;top:373px;display:flex;gap:9px}
.dots span{width:6px;height:6px;border-radius:50%;background:#fff}
.dots span.on{background:transparent;border:1.5px solid #fff}

/* steps */
.lead{left:0;width:801px;top:414px;text-align:center;font-size:14.5px}
.sub{left:0;width:801px;top:435px;text-align:center;font-size:10.5px;color:#333}
.sub b{font-family:"Roboto Condensed",sans-serif;font-weight:400;font-size:16px;color:var(--blue);vertical-align:-2px;margin-left:3px}
.step{top:470px;width:120px;text-align:center;font-size:9.5px;font-weight:500;color:#333}
.step svg{display:block;margin:0 auto 10px}

/* why */
.why{left:0;top:562px;width:801px;height:280px;background:var(--grey-bg)}
.sec-title{font-size:12px;font-weight:700;color:var(--blue);letter-spacing:.2px}
.why-rule{left:107px;top:606px;width:411px;height:1px;background:var(--line)}
.reason{width:190px}
.reason h3{font-size:7.5px;font-weight:700;color:var(--blue);padding-left:13px;position:relative}
.reason h3 svg{position:absolute;left:0;top:0}
.reason p{font-size:6.5px;line-height:1.6;color:#444;margin:5px 0 0 13px}
.car-photo{left:532px;top:600px;width:256px;height:232px;border-radius:40px 40px 14px 14px;background:radial-gradient(ellipse at 50% 55%,#ffffff 0%,#e3e4e6 60%,#c4c6ca 100%)}

/* today */
.tick-list{left:107px;top:895px;list-style:none}
.tick-list li{display:flex;align-items:center;gap:10px;font-size:7.5px;color:#444;height:21px}
.hands{left:292px;top:888px;width:140px;height:124px;border-radius:10px;background:linear-gradient(180deg,#8b8c90,#5f6065)}
.prog{left:462px;width:232px;height:33px;border:1px solid #bfbfbf;background:linear-gradient(#fff,#f2f2f2);display:flex;align-items:center;gap:10px;padding-left:12px;font-size:8.5px;color:#222}

/* footer */
.footer{left:0;top:1072px;width:801px;height:128px;background:var(--blue)}
.f-label{font-size:6.5px;font-weight:700;color:#fff;letter-spacing:.3px}
.social{left:107px;top:1111px;display:flex;gap:4px}
.social span{width:15px;height:15px;border-radius:50%;background:#2d9be0}
.social span:last-child{background:#e8682d}
.menu{left:234px;top:1113px;font-size:6px;color:#fff;word-spacing:1px}
.seals{left:467px;top:1090px;width:226px;height:40px;background:#fff;display:flex;align-items:center;justify-content:space-around;padding:0 10px}
.seal-a{width:70px;height:22px;background:#2f5b7a;border-radius:2px}
.seal-b{width:80px;height:24px;background:#d6d6d6;border-radius:2px}
.seal-c{width:28px;height:28px;border-radius:50%;border:3px solid #8aa6c4}
.f-rule{left:107px;top:1156px;width:587px;height:1px;background:rgba(255,255,255,.2)}
.legal{top:1170px;font-size:6px;color:#fff}
</style>
</head>
<body>

<header>
  <div class="abs brand"><span class="brand-mark"></span><span class="brand-name">Rides for Heroes</span></div>
  <div class="abs help">WE NEED YOUR HELP</div>
  <div class="abs help-phone">
    <svg width="10" height="10" viewBox="0 0 24 24"><path fill="#2a5cae" d="M6.6 10.8a15 15 0 0 0 6.6 6.6l2.2-2.2c.3-.3.7-.4 1-.2 1.1.4 2.3.6 3.6.6.6 0 1 .4 1 1V20c0 .6-.4 1-1 1A17 17 0 0 1 3 4c0-.6.4-1 1-1h3.5c.6 0 1 .4 1 1 0 1.3.2 2.5.6 3.6.1.3 0 .7-.2 1z"/></svg>
    1-800-555-0142
  </div>
  <div class="abs help-days">7 DAYS A WEEK</div>
  <svg class="abs ribbon" width="62" height="80" viewBox="0 0 62 80">
    <path d="M0 0h62v72l-31-8-31 8z" fill="#fff" stroke="#d8d8d8"/>
    <rect x="6" y="4" width="50" height="30" fill="var(--blue)" stroke="#fff"/>
    <rect x="6" y="38" width="50" height="3" fill="#c9d5ea"/>
    <rect x="9" y="45" width="44" height="3" fill="#c9d5ea"/>
    <rect x="12" y="52" width="38" height="3" fill="#c9d5ea"/>
  </svg>
</header>

<nav class="abs nav">
  <a class="active" href="#">HOME</a>
  <a href="#" style="left:177px">ABOUT US</a>
  <a href="#" style="left:262px">WHY DONATE?</a>
  <a href="#" style="left:363px">HOW IT WORKS</a>
  <a href="#" style="left:458px">CONTACT US</a>
</nav>

<section class="abs hero" role="img" aria-label="Photo of a veteran in a wheelchair opening the door of a red car on a brick street"></section>

<form class="abs form">
  <h2>Car Donation Here!</h2>
  <div class="field" style="left:14px;top:52px"><svg width="6" height="6" viewBox="0 0 10 10"><circle cx="5" cy="3" r="2.4" fill="#888"/><path d="M0 10a5 4 0 0 1 10 0z" fill="#888"/></svg>Name</div>
  <div class="field" style="left:120px;top:52px"><svg width="7" height="6" viewBox="0 0 12 9"><rect width="12" height="9" fill="#888"/><path d="M0 0l6 5 6-5" stroke="#f4f4f4" fill="none"/></svg>E mail</div>
  <div class="field" style="left:14px;top:80px"><svg width="6" height="6" viewBox="0 0 24 24"><path fill="#888" d="M6.6 10.8a15 15 0 0 0 6.6 6.6l2.2-2.2c.3-.3.7-.4 1-.2 1.1.4 2.3.6 3.6.6.6 0 1 .4 1 1V20c0 .6-.4 1-1 1A17 17 0 0 1 3 4c0-.6.4-1 1-1h3.5c.6 0 1 .4 1 1 0 1.3.2 2.5.6 3.6.1.3 0 .7-.2 1z"/></svg>Phone</div>
  <div class="field" style="left:120px;top:80px"><svg width="5" height="7" viewBox="0 0 6 10"><rect width="6" height="10" rx="1" fill="#888"/></svg>Mobile</div>
  <div class="field" style="left:14px;top:112px"><svg width="6" height="6" viewBox="0 0 10 10"><path d="M10 0L0 4l4 2 2 4z" fill="#888"/></svg>Address</div>
  <div class="field" style="left:120px;top:112px"><svg width="5" height="7" viewBox="0 0 6 10"><rect width="6" height="10" fill="#888"/></svg>City</div>
  <div class="field" style="left:14px;top:144px"><svg width="6" height="4" viewBox="0 0 10 6"><path d="M0 0l5 6 5-6" stroke="#888" stroke-width="2" fill="none"/></svg>State</div>
  <div class="field" style="left:120px;top:144px"><svg width="5" height="7" viewBox="0 0 10 14"><path d="M5 0a5 5 0 0 1 5 5c0 4-5 9-5 9S0 9 0 5a5 5 0 0 1 5-5z" fill="#888"/></svg>Zip Code</div>
  <div class="donate-btn">DONATE NOW!</div>
</form>
<div class="abs dots"><span></span><span class="on"></span><span></span><span></span><span></span></div>

<section>
  <h1 class="abs lead" style="font-weight:400">Donate Your Car: Full Tax Deduction - Running or Not</h1>
  <p class="abs sub">Please fill out form or Call toll-free <b>1-800-555-0142</b></p>

  <div class="abs step" style="left:157px">
    <svg width="54" height="46" viewBox="0 0 54 46"><path d="M4 16c0-10 46-10 46 0v4h-10v-5c-6-3-20-3-26 0v5H4z" fill="var(--blue)"/><path d="M12 20h30l6 22H6z" fill="#4a4a4a"/><g fill="#fff"><rect x="21" y="26" width="4" height="3"/><rect x="26" y="26" width="4" height="3"/><rect x="31" y="26" width="4" height="3"/><rect x="21" y="31" width="4" height="3"/><rect x="26" y="31" width="4" height="3"/><rect x="31" y="31" width="4" height="3"/></g></svg>
    CALL US
  </div>
  <div class="abs step" style="left:340px">
    <svg width="50" height="46" viewBox="0 0 50 46"><path d="M6 2l14 18" stroke="#444" stroke-width="3"/><path d="M6 2v14" stroke="#444" stroke-width="1.5"/><rect x="4" y="24" width="26" height="12" fill="#444"/><path d="M30 18h10l6 10v8H30z" fill="#444"/><circle cx="12" cy="39" r="5" fill="var(--blue)"/><circle cx="22" cy="39" r="5" fill="var(--blue)"/><circle cx="40" cy="39" r="5" fill="var(--blue)"/></svg>
    WE TOW IT
  </div>
  <div class="abs step" style="left:513px">
    <svg width="40" height="46" viewBox="0 0 40 46"><path d="M2 2h26v42H2z" fill="#fff" stroke="#444" stroke-width="2.5"/><g stroke="#444" stroke-width="2"><path d="M7 12h16M7 18h16M7 24h12M7 30h10"/></g><path d="M36 12L20 34l-3 5 5-3 16-22z" fill="var(--blue)"/></svg>
    TAX WRITE OFF
  </div>
</section>

<section class="abs why"></section>
<h2 class="abs sec-title" style="left:107px;top:584px">WHY DONATE YOUR CAR TO US?</h2>
<div class="abs why-rule"></div>

<div class="abs reason" style="left:107px;top:628px"><h3><svg width="8" height="8" viewBox="0 0 10 10"><circle cx="5" cy="5" r="5" fill="var(--blue)"/><path d="M2.5 5l1.8 1.8 3.2-3.4" stroke="#fff" stroke-width="1.3" fill="none"/></svg>TOP RATED &amp; IRS 501(C)3 APPROVED:</h3><p>Free 24/7 Pickup with No DMV Hassles.</p></div>
<div class="abs reason" style="left:107px;top:675px"><h3><svg width="8" height="8" viewBox="0 0 10 10"><circle cx="5" cy="5" r="5" fill="var(--blue)"/><path d="M2.5 5l1.8 1.8 3.2-3.4" stroke="#fff" stroke-width="1.3" fill="none"/></svg>ALL CARS ACCEPTED</h3><p>We take your car regardless of its condition or registration status.</p></div>
<div class="abs reason" style="left:107px;top:727px"><h3><svg width="8" height="8" viewBox="0 0 10 10"><circle cx="5" cy="5" r="5" fill="var(--blue)"/><path d="M2.5 5l1.8 1.8 3.2-3.4" stroke="#fff" stroke-width="1.3" fill="none"/></svg>NO PAPERWORK HASSLES</h3><p>We take any car and handle everything: DMV, Smog and IRS paperwork.</p></div>
<div class="abs reason" style="left:107px;top:778px"><h3><svg width="8" height="8" viewBox="0 0 10 10"><circle cx="5" cy="5" r="5" fill="var(--blue)"/><path d="M2.5 5l1.8 1.8 3.2-3.4" stroke="#fff" stroke-width="1.3" fill="none"/></svg>SCHEDULE A FREE PICKUP</h3><p>Complete the form and a representative will call you to arrange a convenient time to pickup your car.</p></div>
<div class="abs reason" style="left:324px;top:628px"><h3><svg width="8" height="8" viewBox="0 0 10 10"><circle cx="5" cy="5" r="5" fill="var(--blue)"/><path d="M2.5 5l1.8 1.8 3.2-3.4" stroke="#fff" stroke-width="1.3" fill="none"/></svg>FREE LOCAL TOWING</h3><p>We will pick up your car donation, running or not, when it's most convenient, at home or work.</p></div>
<div class="abs reason" style="left:324px;top:675px"><h3><svg width="8" height="8" viewBox="0 0 10 10"><circle cx="5" cy="5" r="5" fill="var(--blue)"/><path d="M2.5 5l1.8 1.8 3.2-3.4" stroke="#fff" stroke-width="1.3" fill="none"/></svg>INCOME TAX DEDUCTION</h3><p>We issue you an IRS tax receipt &amp; offer the largest resale network to get you the highest tax write-off possible.</p></div>
<div class="abs reason" style="left:324px;top:727px"><h3><svg width="8" height="8" viewBox="0 0 10 10"><circle cx="5" cy="5" r="5" fill="var(--blue)"/><path d="M2.5 5l1.8 1.8 3.2-3.4" stroke="#fff" stroke-width="1.3" fill="none"/></svg>CAR DONATIONS HELP FUND PROGRAMS</h3><p>And benefit National Heroes Support Fund. An IRS 501(c)3 nonprofit organization.</p></div>

<div class="abs car-photo" role="img" aria-label="Photo of a white compact car seen from the front"></div>

<h2 class="abs sec-title" style="left:107px;top:866px">DONATE YOUR CAR TODAY!</h2>
<ul class="abs tick-list">
  <li><svg width="8" height="8" viewBox="0 0 10 10"><circle cx="5" cy="5" r="5" fill="var(--blue)"/><path d="M2.5 5l1.8 1.8 3.2-3.4" stroke="#fff" stroke-width="1.3" fill="none"/></svg>You have no costs.</li>
  <li><svg width="8" height="8" viewBox="0 0 10 10"><circle cx="5" cy="5" r="5" fill="var(--blue)"/><path d="M2.5 5l1.8 1.8 3.2-3.4" stroke="#fff" stroke-width="1.3" fill="none"/></svg>Free towing, running or not.</li>
  <li><svg width="8" height="8" viewBox="0 0 10 10"><circle cx="5" cy="5" r="5" fill="var(--blue)"/><path d="M2.5 5l1.8 1.8 3.2-3.4" stroke="#fff" stroke-width="1.3" fill="none"/></svg>We issue you an IRS tax receipt.</li>
  <li><svg width="8" height="8" viewBox="0 0 10 10"><circle cx="5" cy="5" r="5" fill="var(--blue)"/><path d="M2.5 5l1.8 1.8 3.2-3.4" stroke="#fff" stroke-width="1.3" fill="none"/></svg>We take care of all paperwork.</li>
  <li><svg width="8" height="8" viewBox="0 0 10 10"><circle cx="5" cy="5" r="5" fill="var(--blue)"/><path d="M2.5 5l1.8 1.8 3.2-3.4" stroke="#fff" stroke-width="1.3" fill="none"/></svg>And we take care of DMV &amp; Smog issues.</li>
</ul>
<div class="abs hands" role="img" aria-label="Illustration of two open hands holding a car"></div>

<h2 class="abs sec-title" style="left:461px;top:866px">CAR DONATION PROGRAM</h2>
<div class="abs prog" style="top:890px"><svg width="11" height="11" viewBox="0 0 12 12"><circle cx="6" cy="6" r="5.5" fill="#333"/><path d="M3 4c2 0 2 2 4 2s0 3 2 3" stroke="#fff" fill="none"/></svg>Donation Accepted Nationwide</div>
<div class="abs prog" style="top:932px"><svg width="12" height="10" viewBox="0 0 12 10"><path d="M2 4l1.5-3h5L10 4h1v4H1V4z" fill="#333"/><circle cx="3" cy="8.5" r="1.3" fill="#333"/><circle cx="9" cy="8.5" r="1.3" fill="#333"/></svg>All Vehicle type welcome</div>
<div class="abs prog" style="top:971px"><svg width="9" height="11" viewBox="0 0 9 11"><rect x=".5" y=".5" width="8" height="10" fill="none" stroke="#333"/><rect x="2" y="2" width="5" height="2" fill="#333"/><g fill="#333"><rect x="2" y="5.5" width="1.3" height="1.3"/><rect x="4" y="5.5" width="1.3" height="1.3"/><rect x="6" y="5.5" width="1.3" height="1.3"/><rect x="2" y="8" width="1.3" height="1.3"/><rect x="4" y="8" width="1.3" height="1.3"/><rect x="6" y="8" width="1.3" height="1.3"/></g></svg>Tax Deductible</div>
<div class="abs prog" style="top:1014px"><svg width="16" height="13" viewBox="0 0 50 46"><path d="M6 2l14 18" stroke="#333" stroke-width="4"/><rect x="4" y="24" width="26" height="12" fill="#333"/><path d="M30 18h10l6 10v8H30z" fill="#333"/><circle cx="12" cy="39" r="5" fill="#333"/><circle cx="40" cy="39" r="5" fill="#333"/></svg>Towing is free</div>

<footer class="abs footer"></footer>
<div class="abs f-label" style="left:107px;top:1095px">FOLLOW US ON</div>
<div class="abs social"><span></span><span></span><span></span><span></span></div>
<div class="abs f-label" style="left:234px;top:1097px">MENU</div>
<div class="abs menu">HOME &nbsp;| &nbsp;ABOUT US &nbsp;| &nbsp;WHY DONATE? &nbsp;| &nbsp;HOW IT WORKS &nbsp;| &nbsp;CONTACT US</div>
<div class="abs seals"><span class="seal-a"></span><span class="seal-b"></span><span class="seal-c"></span></div>
<div class="abs f-rule"></div>
<div class="abs legal" style="left:108px">Privacy Policy &nbsp;| &nbsp;Terms &amp; Conditions</div>
<div class="abs legal" style="left:581px">Copyrights @ 2016 All Rights Reserved</div>

</body>
</html>
```